Professional law firm looking for new professional and eye-catching business card design

Law firm in need of new business card design using existing firm logo and firm colors on thick card stock. Firm colors are navy blue, cyan blue, and gray. Please use firm's logo either on the back of the card or on the front and back. I am looking for something eye-catching and resonating but also professional.

Target Market(s)

Law firm growth by attracting clients with professional, creative, and attractive business cards.

Industry/Entity Type

Legal/Law Firm

Contact Information for Business Card

Name: Derek T. Halloway, Esq., Address: 517 E. Quintley Blvd., P.O. Box 641, Alderwick, ST 00790, Phone numbers: (555) 555-0187 Office, (555) 555-0142 Fax, email address: DerekH@hqlegalfx.com, website: www.HQLegalFX.com

Font styles to use
Other font styles liked:
• Font as close as possible to matching law firm logo.

Requirements
Must have
• Must have business card details and law firm logo with law firm colors.

```html
<!DOCTYPE html>
<html lang="en">
<head>
<meta charset="utf-8">
<title>HQ Legal Business Card</title>
<link rel="stylesheet" href="https://fonts.googleapis.com/css2?family=Alegreya:wght@400;700&display=swap">
<style>
  :root {
    --backdrop: #b2c4cb;
    --card-cyan: #00adef;
    --ink-white: #ffffff;
    --figure-tone: rgba(255, 255, 255, 0.82);
  }
  * { margin: 0; padding: 0; box-sizing: border-box; }
  html, body {
    width: 1200px; height: 1085px; overflow: hidden;
    background: var(--backdrop);
    font-family: "Alegreya", Georgia, serif;
    color: var(--ink-white);
  }
  .card {
    position: absolute; left: 301px; width: 578px; height: 343px;
    background: var(--card-cyan);
  }
  .card-front { top: 163px; }
  .card-back { top: 542px; }

  .figure-area {
    position: absolute; background: var(--figure-tone); border-radius: 30px 30px 8px 8px;
  }
  .card-front .figure-area { left: 38px; top: 74px; width: 54px; height: 183px; }
  .card-back .figure-area { left: 160px; top: 45px; width: 72px; height: 254px; }

  .firm-mark { position: absolute; text-align: right; }
  .firm-name { font-weight: 400; letter-spacing: 1px; line-height: 1; display: block; white-space: nowrap; }
  .firm-rule { display: block; border-top: 1px solid var(--ink-white); }
  .firm-sub { display: block; font-weight: 400; line-height: 1; font-variant: small-caps; white-space: nowrap; }

  .card-front .firm-mark { left: 98px; top: 162px; width: 126px; }
  .card-front .firm-name { font-size: 27px; padding-bottom: 6px; }
  .card-front .firm-rule { margin-bottom: 5px; }
  .card-front .firm-sub { font-size: 11.5px; }

  .card-back .firm-mark { left: 239px; top: 168px; width: 179px; }
  .card-back .firm-name { font-size: 38px; padding-bottom: 8px; }
  .card-back .firm-rule { margin-bottom: 9px; }
  .card-back .firm-sub { font-size: 16px; }

  .divider {
    position: absolute; left: 247px; top: 63px; width: 1px; height: 208px;
    background: var(--ink-white);
  }
  .details { position: absolute; left: 265px; top: 64px; width: 305px; }
  .person-name { font-size: 20px; font-weight: 700; text-transform: uppercase; letter-spacing: 0.4px; line-height: 1.05; white-space: nowrap; }
  .person-title { font-size: 16px; letter-spacing: 1.5px; line-height: 1.15; }
  .short-rule { width: 62px; border-top: 1px solid var(--ink-white); margin: 12px 0 9px 2px; }
  .contact-list { list-style: none; }
  .contact-list li {
    display: flex; align-items: center; gap: 6px;
    font-size: 17px; letter-spacing: 1.1px; line-height: 19px; white-space: nowrap;
  }
  .contact-list svg { width: 14px; height: 14px; flex: none; }
  .address { font-size: 17px; letter-spacing: 1.2px; line-height: 19px; margin-left: 3px; white-space: nowrap; }
</style>
</head>
<body>
  <section class="card card-front">
    <div class="figure-area" role="img" aria-label="Illustration of a blindfolded justice figure holding scales and a sword"></div>
    <div class="firm-mark">
      <span class="firm-name">HQ LEGAL</span>
      <span class="firm-rule"></span>
      <span class="firm-sub">Halloway + Quintley, P.A.</span>
    </div>
    <div class="divider"></div>
    <div class="details">
      <p class="person-name">Derek T. Halloway, Esq.,</p>
      <p class="person-title">Managing Director</p>
      <div class="short-rule"></div>
      <ul class="contact-list">
        <li><svg viewBox="0 0 16 16" aria-hidden="true"><path fill="#fff" d="M3 1.5l2.5 3-1.4 1.6c.8 1.9 2.1 3.2 4 4l1.6-1.4 3 2.5-1.6 2.3C6.6 13.3 2.7 9.4 1 4.9z"/></svg>(555) 555-0187 (Office)</li>
        <li><svg viewBox="0 0 16 16" aria-hidden="true"><path fill="#fff" d="M4 1h8v4H4zM1 6h14v6h-3v3H4v-3H1zm4 4v3h6v-3z"/></svg>(555) 555-0142</li>
        <li><svg viewBox="0 0 16 16" aria-hidden="true"><path fill="#fff" d="M1 3h14v10H1zm1.5 1.2L8 8.5l5.5-4.3z"/></svg>DerekH@hqlegalfx.com</li>
        <li><svg viewBox="0 0 16 16" aria-hidden="true"><g fill="none" stroke="#fff" stroke-width="1.3"><circle cx="8" cy="8" r="6.5"/><ellipse cx="8" cy="8" rx="2.8" ry="6.5"/><path d="M1.5 8h13M2.5 4.8h11M2.5 11.2h11"/></g></svg>www.HQLegalFX.com</li>
      </ul>
      <div class="short-rule"></div>
      <p class="address">517 E. Quintley Blvd.,<br>P.O. Box 641, Alderwick, ST 00790</p>
    </div>
  </section>

  <section class="card card-back">
    <div class="figure-area" role="img" aria-label="Illustration of a blindfolded justice figure holding scales and a sword"></div>
    <div class="firm-mark">
      <span class="firm-name">HQ LEGAL</span>
      <span class="firm-rule"></span>
      <span class="firm-sub">Halloway + Quintley, P.A.</span>
    </div>
  </section>
</body>
</html>
```